Webdesign für Kfz-Betrieb
Zielgruppe
Seit über 20 Jahren ist Fahrpunkt Wellbrock die erste Anlaufstelle wenn es um die Themen Reifen, Felgen und den gesamten Kfz-Bereich geht. Außerdem ist das Unternehmen seit 1997 auf Fahrzeugaufbereitung spezialisiert.
ZG: Alle, die Reifen benötigen
Aufgabenstellung
Layout Adobe Photoshop
hell, freundlich, aufgeschlossen
Die Leistungen sollen mit Icons dargestellt werden. (siehe Welche Inhalte sollen angezeigt werden)
Logo liegt noch nicht vor
nur die Startseite layouten

```html
<!DOCTYPE html>
<html lang="en">
<head>
<meta charset="utf-8">
<title>Fahrpunkt Wellbrock – Auto Parts &amp; Service</title>
<link rel="stylesheet" href="https://fonts.googleapis.com/css2?family=Poppins:wght@400;500;600;700&display=swap">
<style>
:root{
  --red:#e30613;
  --green:#17a23c;
  --green-dark:#1c7a1f;
  --ink:#1d1d1d;
  --muted:#8a8a8a;
  --light:#eeeeee;
  --footer:#1b1b1b;
  --bar:#0f3d12;
}
*{box-sizing:border-box;margin:0;padding:0}
html,body{width:1200px;height:5081px;overflow:hidden}
body{position:relative;font-family:'Poppins',sans-serif;color:var(--ink);background:#fff}
.abs{position:absolute}
.ph{position:absolute}
.section-mark{position:absolute;width:44px;height:44px;border:7px solid var(--red);border-radius:50%}
.h2{position:absolute;font-weight:700;font-size:40px;letter-spacing:1px;text-align:center;left:0;width:1200px}
.rule{position:absolute;height:4px;width:82px;background:var(--red)}
.lead{position:absolute;font-size:12.5px;line-height:22px;color:var(--muted);text-align:center}
.body-text{position:absolute;font-size:12.5px;line-height:21px;color:var(--muted);text-align:justify}
.btn-outline{position:absolute;border:2px solid var(--green);color:var(--green);font-weight:600;font-size:15px;display:flex;align-items:center;justify-content:center;background:#fff}

/* header */
.brand{position:absolute;left:112px;top:30px;display:flex;align-items:center;gap:10px;font-weight:700;font-size:26px;color:var(--green)}
.brand i{width:22px;height:22px;background:var(--red);border-radius:50%;display:block}
.callus{left:630px;top:11px;font-size:15px;font-weight:600}
.callus span{color:var(--red);font-weight:500}
.appt-top{left:870px;top:0;width:218px;height:38px;background:var(--red);color:#fff;font-weight:600;font-size:14px;display:flex;align-items:center;justify-content:center;gap:8px}
.nav{left:433px;top:60px;display:flex;gap:24px;font-size:13px;font-weight:500}
.nav .active{color:var(--red)}
.dropdown{left:498px;top:115px;width:219px;background:#fff;box-shadow:0 4px 10px rgba(0,0,0,.15);font-size:13px;font-weight:500}
.dropdown div{height:35px;padding-left:18px;display:flex;align-items:center;border-bottom:1px solid #e4e4e4}

/* hero */
.hero{left:0;top:105px;width:1200px;height:495px;background:linear-gradient(90deg,#2a2a2a,#5b5b5b 55%,#4a4039)}
.hero-title{left:112px;top:345px;color:#fff;font-weight:700;font-size:58px;line-height:68px}
.hero-sub{left:112px;top:492px;width:390px;color:#fff;font-size:11px;line-height:21px}
.form{left:780px;top:313px;width:317px;height:417px;background:#fff;box-shadow:0 4px 18px rgba(0,0,0,.18);padding:20px 18px}
.form h3{color:var(--red);font-size:32px;font-weight:700;line-height:36px}
.form small{display:block;font-size:9px;color:var(--muted);margin:6px 0 14px}
.form .field{height:30px;border:1px solid #d6d6d6;font-size:9px;color:#999;padding:8px;margin-bottom:12px}
.form .area{height:78px}
.form .submit{height:28px;background:var(--green);color:#fff;font-size:10px;display:flex;align-items:center;justify-content:center}

/* steps */
.step{position:absolute;width:240px;text-align:center;font-size:20px;font-weight:500;line-height:32px;letter-spacing:.5px}

/* news */
.news-band{left:0;top:2690px;width:1200px;height:475px;background:linear-gradient(90deg,#1a1a1a,#3a3a3a 60%,#222)}
.news-label{position:absolute;background:var(--green-dark);color:#fff;font-weight:600;font-size:20px;line-height:26px;text-align:center;display:flex;align-items:center;justify-content:center}

/* faq */
.faq{position:absolute;left:112px;width:475px;height:48px;background:#efefef;font-size:13px;font-weight:500;display:flex;align-items:center;justify-content:space-between;padding:0 20px 0 30px}

/* footer */
.footer{left:0;top:4650px;width:1200px;height:365px;background:var(--footer);color:#fff}
.fcol h4{font-size:22px;font-weight:600}
.fcol .uline{width:104px;height:2px;background:#fff;margin:8px 0 22px}
.fcol a{display:block;color:#fff;text-decoration:none;font-size:12px;line-height:31px}
.bottom-bar{left:0;top:5015px;width:1200px;height:66px;background:var(--bar);color:#fff;font-size:11px;display:flex;align-items:center;padding:0 112px;justify-content:space-between}
.bottom-bar nav{display:flex;gap:42px;font-size:14px}
</style>
</head>
<body>

<!-- header -->
<div class="brand"><i></i>Fahrpunkt Wellbrock</div>
<div class="abs callus">CALL US : <span>0341 / 55 20 16</span></div>
<div class="abs appt-top">
  <svg width="18" height="18" viewBox="0 0 18 18"><circle cx="9" cy="9" r="7.5" fill="none" stroke="#fff" stroke-width="1.8"/><path d="M9 5v8M5 9h8" stroke="#fff" stroke-width="1.8"/></svg>APPOINTMENT</div>
<nav class="abs nav"><span class="active">HOME</span><span>SERVICES</span><span>APPOINTMENT ARRANGEMENT</span><span>COMPANY</span><span>NEWS</span><span>COMMITMENT</span></nav>

<!-- hero -->
<div class="ph hero" role="img" aria-label="Workshop background with a mechanic holding a tyre"></div>
<div class="abs dropdown">
  <div>STORAGE</div><div>VEHICLE PREPARATION</div><div>VEHICLE INSPECTION</div><div>WHEEL WASH</div><div>NITROGEN FILLING</div>
</div>
<div class="abs hero-title">THE World's Best<br>AUTO PARTS</div>
<p class="abs hero-sub">Lorem Ipsum is simply dummy text of the printing and typesetting industry. Lorem Ipsum has been the industry's standard dummy text ever since the 1500s</p>
<form class="abs form">
  <h3>Get In Touch</h3>
  <small>Contact us for custom quote</small>
  <div class="field">Your name</div>
  <div class="field">Your Email Address</div>
  <div class="field">Your Phone Number (optional)</div>
  <div class="field">Your Web Site (optional)</div>
  <div class="field area">Type your message here.....</div>
  <div class="submit">Submit</div>
</form>

<!-- how it works -->
<div class="section-mark" style="left:578px;top:622px"></div>
<h2 class="h2" style="top:675px">HOW IT WORKS</h2>
<div class="rule" style="left:559px;top:740px"></div>
<p class="lead" style="left:250px;top:768px;width:700px">Lorem Ipsum is simply dummy text of the printing and typesetting industry. Lorem Ipsum has been the industry's standard dummy text ever since the 1500s</p>

<svg class="abs" style="left:183px;top:870px" width="76" height="100" viewBox="0 0 76 100">
  <g fill="none" stroke="var(--red)" stroke-width="2.5">
    <rect x="2" y="4" width="14" height="14"/><rect x="2" y="28" width="14" height="14"/><rect x="2" y="52" width="14" height="14"/><rect x="2" y="76" width="14" height="14"/>
  </g>
  <g stroke="#333" stroke-width="2.5" fill="none"><path d="M5 11l3 3 6-7M5 35l3 3 6-7M5 59l3 3 6-7M5 83l3 3 6-7"/><path d="M26 11h48M26 35h48M26 59h48M26 83h48"/></g>
</svg>
<div class="abs" style="left:378px;top:890px;width:162px;height:46px;background:#444;color:#fff;font-size:11px;font-weight:600;display:flex;align-items:center;justify-content:center;gap:8px">
  <svg width="16" height="16" viewBox="0 0 16 16"><circle cx="8" cy="8" r="6.5" fill="none" stroke="#fff" stroke-width="1.5"/><path d="M8 4.5v7M4.5 8h7" stroke="#fff" stroke-width="1.5"/></svg>APPOINTMENT</div>
<div class="ph" style="left:632px;top:870px;width:172px;height:95px;background:linear-gradient(180deg,#f2f2f2,#c9c9c9)" role="img" aria-label="White sports car"></div>
<div class="ph" style="left:870px;top:860px;width:125px;height:110px;background:linear-gradient(135deg,#d4d4d4,#4a4a4a)" role="img" aria-label="Car keys with remote"></div>
<div class="step" style="left:106px;top:990px">Choose Your<br>SERVICE</div>
<div class="step" style="left:350px;top:990px">Make an<br>APPOINTMENT</div>
<div class="step" style="left:602px;top:990px">We'll take Your<br>CAR for REPAIR</div>
<div class="step" style="left:826px;top:990px">PICK UP Your<br>CAR KEYS</div>

<!-- about -->
<div class="abs" style="left:0;top:1100px;width:1200px;height:690px;background:var(--light)"></div>
<div class="abs" style="left:0;top:1133px;width:405px;height:615px;background:var(--red)"></div>
<div class="ph" style="left:133px;top:1210px;width:430px;height:462px;background:linear-gradient(160deg,#9a9a9a,#3c3c3c 55%,#1c1c1c)" role="img" aria-label="Mechanic's gloved hand fitting a tyre on a wheel"></div>
<div class="section-mark" style="left:668px;top:1252px"></div>
<h2 class="abs" style="left:668px;top:1308px;font-size:40px;font-weight:700;letter-spacing:1px">ABOUT US</h2>
<p class="body-text" style="left:668px;top:1398px;width:416px">Lorem Ipsum is simply dummy text of the printing and typesetting industry. Lorem Ipsum has been the industry's standard dummy text ever since the 1500s</p>
<p class="body-text" style="left:668px;top:1490px;width:416px">Lorem Ipsum is simply dummy text of the printing and typesetting industry. Lorem Ipsum has been the industry's standard dummy text ever since the 1500s</p>
<div class="btn-outline" style="left:668px;top:1587px;width:166px;height:45px">Learn More</div>

<!-- services -->
<div class="section-mark" style="left:578px;top:1817px"></div>
<h2 class="h2" style="top:1870px">OUR SERVICES</h2>
<div class="rule" style="left:559px;top:1936px"></div>
<div class="abs" style="left:599px;top:1982px;width:2px;height:668px;background:#d6d6d6"></div>

<h3 class="abs" style="left:105px;top:1970px;font-size:24px;font-weight:600">STORAGE</h3>
<p class="body-text" style="left:105px;top:2018px;width:342px">Lorem Ipsum is simply dummy text of the printing and typesetting industry. Lorem Ipsum has been the industry's standard dummy text ever since the 1500s, when an unknown printer took a galley of type and scrambled it to make a type specimen book. It has survived not only five centuries, but also the leap into electronic typesetting, remaining essentially unchanged.Lorem Ipsum is simply dummy text of the printing and typesetting industry. Lorem Ipsum has been the industry's standard dummy text ever since</p>
<div class="abs" style="left:521px;top:1980px;width:158px;height:158px;border-radius:50%;background:#fff;border:2px solid #d6d6d6;display:flex;align-items:center;justify-content:center">
  <svg width="80" height="72" viewBox="0 0 80 72" fill="none" stroke="var(--red)" stroke-width="3.5"><path d="M4 28L40 4l36 24v40H4z"/><path d="M16 66V34h48v32"/><rect x="24" y="44" width="32" height="14" rx="4"/><path d="M28 44l4-6h16l4 6"/></svg>
</div>
<div class="ph" style="left:740px;top:1980px;width:348px;height:268px;background:linear-gradient(135deg,#2b2b2b,#8c8c8c 50%,#e0e0e0)" role="img" aria-label="Inspector with clipboard next to a car"></div>

<div class="ph" style="left:110px;top:2288px;width:348px;height:270px;background:linear-gradient(135deg,#cfcfcf,#6f6f6f 50%,#2d2d2d)" role="img" aria-label="Steel storage racks in a warehouse"></div>
<div class="abs" style="left:521px;top:2287px;width:158px;height:158px;border-radius:50%;background:#fff;border:2px solid #d6d6d6;display:flex;align-items:center;justify-content:center">
  <svg width="92" height="52" viewBox="0 0 92 52"><path d="M6 34l6-14 16-10h30l16 12 12 4v12H6z" fill="var(--red)"/><circle cx="22" cy="40" r="8" fill="#fff" stroke="var(--red)" stroke-width="4"/><circle cx="70" cy="40" r="8" fill="#fff" stroke="var(--red)" stroke-width="4"/></svg>
</div>
<h3 class="abs" style="left:733px;top:2280px;font-size:24px;font-weight:600">VEHICLE PREPARATION</h3>
<p class="body-text" style="left:733px;top:2328px;width:355px">Lorem Ipsum is simply dummy text of the printing and typesetting industry. Lorem Ipsum has been the industry's standard dummy text ever since the 1500s, when an unknown printer took a galley of type and scrambled it to make a type specimen book. It has survived not only five centuries, but also the leap into electronic typesetting, remaining essentially unchanged.Lorem Ipsum is simply dummy text of the printing and typesetting industry. Lorem Ipsum has been the industry's</p>
<div class="btn-outline" style="left:517px;top:2610px;width:166px;height:45px">Learn More</div>

<!-- latest news -->
<div class="ph news-band" role="img" aria-label="Dark workshop background"></div>
<div class="section-mark" style="left:115px;top:2722px;border-color:#fff"></div>
<h2 class="abs" style="left:112px;top:2778px;color:#fff;font-size:40px;font-weight:600;letter-spacing:1px">LATEST NEWS</h2>
<div class="abs" style="left:112px;top:2843px;width:82px;height:4px;background:#fff"></div>
<p class="abs" style="left:588px;top:2732px;width:500px;color:#fff;font-size:11.5px;font-weight:600;line-height:23px;text-align:justify">Lorem Ipsum is simply dummy text of the printing and typesetting industry. Lorem Ipsum has been the industry's standard dummy text ever since the 1500s Lorem Ipsum is simply dummy text of the printing and typesetting industry. Lorem Ipsum has been the industry's standard dummy text ever since the 1500s</p>

<div class="ph" style="left:135px;top:2930px;width:302px;height:235px;background:linear-gradient(135deg,#d8d8d8,#555 60%,#222)" role="img" aria-label="Stack of new tyres"></div>
<div class="news-label" style="left:135px;top:3165px;width:302px;height:73px">9 Ways to Protect<br>your TIRES</div>
<div class="ph" style="left:765px;top:2930px;width:298px;height:235px;background:linear-gradient(135deg,#8a8a8a,#3b3b3b 55%,#c9c9c9)" role="img" aria-label="Mechanic changing a wheel"></div>
<div class="news-label" style="left:765px;top:3165px;width:298px;height:73px">Expert in Tyres and<br>Wheels</div>
<div class="ph" style="left:440px;top:2893px;width:325px;height:307px;border:4px solid #fff;background:linear-gradient(135deg,#3a3a3a,#8e1a1a 50%,#5a5a5a)" role="img" aria-label="Red performance alloy rim close-up"></div>
<div class="news-label" style="left:440px;top:3200px;width:325px;height:66px">Extreme Performance<br>RIMS</div>
<svg class="abs" style="left:88px;top:3010px" width="24" height="48" viewBox="0 0 24 48"><path d="M20 4L4 24l16 20" fill="none" stroke="#fff" stroke-width="2.5"/></svg>
<svg class="abs" style="left:1088px;top:3010px" width="24" height="48" viewBox="0 0 24 48"><path d="M4 4l16 20L4 44" fill="none" stroke="#fff" stroke-width="2.5"/></svg>

<!-- commitment -->
<div class="section-mark" style="left:578px;top:3292px"></div>
<h2 class="h2" style="top:3343px">OUR COMMITMENT</h2>
<p class="lead" style="left:250px;top:3440px;width:700px">Lorem Ipsum is simply dummy text of the printing and typesetting industry. Lorem Ipsum has been the industry's standard dummy text ever since the 1500s</p>

<div class="abs" style="left:790px;top:3532px;width:410px;height:658px;background:var(--red)"></div>
<div class="ph" style="left:633px;top:3590px;width:429px;height:505px;background:linear-gradient(160deg,#8a8a8a,#3a3a3a 55%,#111)" role="img" aria-label="Motor oil being poured into an engine"></div>

<div class="faq" style="top:3595px">How often should I get my oil changed?<svg width="22" height="12" viewBox="0 0 22 12"><path d="M1 1l10 10L21 1" fill="none" stroke="var(--red)" stroke-width="1.8"/></svg></div>
<p class="body-text" style="left:112px;top:3660px;width:475px;text-align:left">For a long time and sometimes still today, standard practice at many lube shops is to suggest oil changes every three months or 3,000 miles. In order to know when the best time to get your oil changed is, check the owner's manual of your specific model for manufacturer-recommended intervals.</p>
<div class="faq" style="top:3806px">Should I worry about servicing my leased vehicle?<svg width="22" height="12" viewBox="0 0 22 12"><path d="M1 1l10 10L21 1" fill="none" stroke="#333" stroke-width="1.8"/></svg></div>
<div class="faq" style="top:3866px">Charge my battery after I jump-start my vehicle?<svg width="22" height="12" viewBox="0 0 22 12"><path d="M1 1l10 10L21 1" fill="none" stroke="#333" stroke-width="1.8"/></svg></div>
<div class="faq" style="top:3926px">How do I know when I need new brakes?<svg width="22" height="12" viewBox="0 0 22 12"><path d="M1 1l10 10L21 1" fill="none" stroke="#333" stroke-width="1.8"/></svg></div>
<div class="faq" style="top:3986px">We offer full service auto repair &amp; maintenance?<svg width="22" height="12" viewBox="0 0 22 12"><path d="M1 1l10 10L21 1" fill="none" stroke="#333" stroke-width="1.8"/></svg></div>
<div class="faq" style="top:4047px">We aim a long term relationship with you?<svg width="22" height="12" viewBox="0 0 22 12"><path d="M1 1l10 10L21 1" fill="none" stroke="#333" stroke-width="1.8"/></svg></div>

<!-- we are the best -->
<div class="section-mark" style="left:578px;top:4192px"></div>
<h2 class="h2" style="top:4243px">WE ARE THE BEST!</h2>
<div class="ph" style="left:475px;top:4340px;width:250px;height:285px;background:linear-gradient(160deg,#5a5a5a,#1d1d1d 70%,#b3121a)" role="img" aria-label="Tyre with alloy wheel on a red base"></div>
<div class="abs" style="left:195px;top:4358px;font-size:21px;font-weight:600">Fast Low Cost Freight</div>
<p class="lead" style="left:195px;top:4398px;width:230px;font-size:10px;line-height:22px;text-align:left">Lorem Ipsum is simply dummy text of the printing and typesetting industry.</p>
<div class="abs" style="left:195px;top:4482px;font-size:21px;font-weight:600">Lergest Range</div>
<p class="lead" style="left:195px;top:4522px;width:230px;font-size:10px;line-height:22px;text-align:left">Lorem Ipsum is simply dummy text of the printing and typesetting industry.</p>
<div class="abs" style="left:775px;top:4358px;width:230px;font-size:21px;font-weight:600;text-align:right">Customer Service</div>
<p class="lead" style="left:775px;top:4398px;width:230px;font-size:10px;line-height:22px;text-align:right">Lorem Ipsum is simply dummy text of the printing and typesetting industry.</p>
<div class="abs" style="left:745px;top:4482px;width:260px;font-size:21px;font-weight:600;text-align:right">20 Years in Business</div>
<p class="lead" style="left:775px;top:4522px;width:230px;font-size:10px;line-height:22px;text-align:right">The company has also specialized in vehicle preparation since 1997</p>

<!-- footer -->
<div class="abs footer">
  <div class="abs" style="left:112px;top:72px;display:flex;align-items:center;gap:10px;font-weight:700;font-size:22px;color:#fff"><i style="width:18px;height:18px;background:var(--red);border-radius:50%;display:block"></i>Fahrpunkt Wellbrock</div>
  <p class="abs" style="left:112px;top:152px;width:245px;font-size:12px;line-height:22px">Lorem Ipsum is simply dummy text of the printing and typesetting industry. orem Ipsum has been the industry's standard dummy text ever since the 1500s, when an unknown printer took</p>
  <div class="abs fcol" style="left:418px;top:78px"><h4>Support</h4><div class="uline"></div><a>Support</a><a>Help &amp; FAQ</a><a>Contact Us</a><a>Pricing &amp; Plans</a><a>Cookie Policy</a></div>
  <div class="abs fcol" style="left:622px;top:78px"><h4>Company</h4><div class="uline"></div><a>About Us</a><a>Career</a><a>Our Company</a><a>Service</a></div>
  <div class="abs fcol" style="left:842px;top:78px"><h4>Get In Touch</h4><div class="uline"></div>
    <p style="font-size:12px;line-height:21px;padding-left:4px">Fahrpunkt Wellbrock<br>Lindenweg 12<br>04109 Talberg</p>
    <div style="display:flex;align-items:center;gap:14px;margin-top:18px;font-size:12px;font-weight:600">
      <svg width="26" height="22" viewBox="0 0 26 22" fill="none" stroke="#fff" stroke-width="1.8"><rect x="2" y="8" width="22" height="12" rx="2"/><path d="M6 8V2h14v6M9 13h8"/></svg>0341 / 55 20 17</div>
    <div style="display:flex;align-items:center;gap:14px;margin-top:18px;font-size:12px;font-weight:600">
      <svg width="26" height="20" viewBox="0 0 26 20" fill="none" stroke="#fff" stroke-width="1.8"><rect x="1.5" y="1.5" width="23" height="17"/><path d="M1.5 1.5L13 11 24.5 1.5"/></svg>service@fahrpunkt-wellbrock.de</div>
  </div>
</div>
<div class="abs bottom-bar">
  <span>© 2022 www.fahrpunkt-wellbrock.de/- ALL RIGHTS RESERVED. PRIVACY POLICY</span>
  <nav><span>COMMUNITY</span><span>NEWSFEED</span><span>GALLERY</span></nav>
</div>

</body>
</html>
```